Business Card design for construction company

I would like a business card design for a construction company - Harlow Constructions. I have attached the ai logo file for use. I would like the card to be very smart and clean and incorporate only white and the two colours in the logo. I would like the card to have two sides. One side can just have the logo, the other with the relevant information.

Target Market(s)

Building and Construction Clients

Industry/Entity Type

Business

Contact Information for Business Card

Name: Tom Pardoe
Company: Harlow Constructions Pty Limited
Address: 14 Mallee Crescent Carrow Vale 2093
Phone: 0427 531 068
Email: tomp@harlowbuild-example.com.au

Font styles to use
Serif
Sans Serif

Requirements
Must have
• Details noted above
• Logo as provided
• Colours as in logo
• Square edges
• A font that compliments the logo
Should not have
• Any colour other than white and those in logo
• Rounded edges

```html
<!DOCTYPE html>
<html lang="en">
<head>
<meta charset="utf-8">
<title>Harlow Constructions – Business Card</title>
<link rel="stylesheet" href="https://fonts.googleapis.com/css2?family=Open+Sans:wght@400;600;700&display=swap">
<style>
  :root {
    --brand-blue: #1e9ad6;
    --brand-charcoal: #3b3c3f;
    --paper: #ffffff;
    --paper-shade: #eeeff0;
    --backdrop: #d9dadc;
    --ink-light: #d3d4d6;
  }
  * { margin: 0; padding: 0; box-sizing: border-box; }
  html, body { width: 1200px; height: 892px; overflow: hidden; }
  body {
    background: var(--backdrop);
    font-family: "Open Sans", Arial, sans-serif;
    position: relative;
  }
  .card {
    position: absolute;
    left: 300px;
    width: 600px;
    height: 367px;
    background: linear-gradient(160deg, var(--paper) 55%, var(--paper-shade));
    box-shadow: 0 6px 18px rgba(0,0,0,0.18);
    overflow: hidden;
  }
  .card--front { top: 50px; }
  .card--back { top: 470px; }
  .card-shapes { position: absolute; inset: 0; width: 600px; height: 367px; }
  .wordmark {
    position: absolute;
    left: 0; right: 0;
    text-align: center;
    color: var(--brand-charcoal);
    font-weight: 600;
    letter-spacing: 0.14em;
    text-transform: uppercase;
  }
  .card--front .wordmark { top: 168px; font-size: 26px; }
  .card--back .wordmark { top: 92px; font-size: 20px; }
  .company-legal {
    position: absolute;
    top: 126px; left: 0; right: 0;
    text-align: center;
    font-size: 11px;
    font-weight: 600;
    color: var(--brand-charcoal);
  }
  .holder-name {
    position: absolute;
    left: 190px; width: 220px;
    top: 181px; height: 50px;
    line-height: 50px;
    text-align: center;
    color: var(--paper);
    font-weight: 700;
    font-size: 25px;
    letter-spacing: 0.04em;
    text-transform: uppercase;
  }
  .contact {
    position: absolute;
    top: 262px;
    color: var(--ink-light);
    font-size: 14px;
    line-height: 26px;
    list-style: none;
  }
  .contact--direct { left: 34px; }
  .contact--address { left: 384px; }
  .contact li { display: flex; align-items: flex-start; gap: 8px; }
  .contact svg { width: 13px; height: 13px; margin-top: 6px; flex: none; fill: var(--ink-light); }
  .contact--address .lines { line-height: 22px; padding-top: 2px; }
</style>
</head>
<body>

<section class="card card--front" aria-label="Card front">
  <svg class="card-shapes" viewBox="0 0 600 367" aria-hidden="true">
    <polygon fill="var(--brand-blue)" points="0,0 600,0 600,9 300,9 282,28 22,28 0,10"/>
    <polygon fill="var(--brand-blue)" points="0,358 230,358 248,340 580,340 600,356 600,367 0,367"/>
  </svg>
  <div class="wordmark">Harlow Constructions</div>
</section>

<section class="card card--back" aria-label="Card back">
  <svg class="card-shapes" viewBox="0 0 600 367" aria-hidden="true">
    <rect x="0" y="206" width="600" height="161" fill="var(--brand-charcoal)"/>
    <rect x="0" y="202" width="600" height="4" fill="var(--brand-blue)"/>
    <polygon fill="var(--brand-blue)" points="204,176 396,176 410,190 410,236 396,240 204,240 190,236 190,190"/>
  </svg>
  <div class="wordmark">Harlow Constructions</div>
  <div class="company-legal">Harlow Constructions Pty Limited</div>
  <div class="holder-name">Tom Pardoe</div>

  <ul class="contact contact--direct">
    <li>
      <svg viewBox="0 0 16 16" aria-hidden="true"><path d="M3 1l3 3-2 2c1 2 3 4 5 5l2-2 3 3-2 2C7 14 2 9 1 3z"/></svg>
      <span>0427 531 068</span>
    </li>
    <li>
      <svg viewBox="0 0 16 16" aria-hidden="true"><path d="M1 3h14v10H1z M1 3l7 6 7-6" stroke="var(--brand-charcoal)" stroke-width="1.2"/></svg>
      <span>tomp@harlowbuild-example.com.au</span>
    </li>
  </ul>

  <ul class="contact contact--address">
    <li>
      <svg viewBox="0 0 16 16" aria-hidden="true"><path d="M8 1L1 7h2v8h4v-5h2v5h4V7h2z"/></svg>
      <span class="lines">14 Mallee Crescent<br>Carrow Vale 2093</span>
    </li>
  </ul>
</section>

</body>
</html>
```